Business Card Design Project

I am opening a skin care studio called Glow Haven by Marisol. I will be offering a wide range of unique and affordable skin services including facials, chemical peels, microdermabrasion treatments, body wraps, salt glows, all waxing and eye lash extensions. If the business cards depicts what I would like, this would lead to brochures, web design, signs, etc.
Updates

Project Deadline Extended
Reason: A request to extend deadline was requested. I will be more than happy to accommodate.

Industry/Entity Type

Business

Requirements
Nice to have
• facial features so prospective client clearly identifies what type of business this is. Not stuffy or boring "spa" looking graphics. I am focusing just on face, body, waxing, eyelashes. No massage or nails.

```html
<!DOCTYPE html>
<html lang="en">
<head>
<meta charset="utf-8">
<title>Glow Haven by Marisol — Business Cards</title>
<link rel="stylesheet" href="https://fonts.googleapis.com/css2?family=Caveat:wght@500&family=Gochi+Hand&family=Just+Me+Again+Down+Here&display=swap">
<style>
  :root {
    --page: #f3efe9;
    --rule: #6f767c;
    --text: #222;
    --name: #6b6b6b;
    --lilac: #f2e4f6;   --lilac-ink: #9a45d6;
    --aqua: #c9f0f1;    --aqua-ink: #2446d8;
    --cream: #f8f5d8;   --cream-ink: #f29490;
    --mint: #cdf6c5;    --mint-ink: #4ed12c;
    --coral: #f8845f;   --coral-ink: #e0201a;
    --divider: #68747e;
  }
  * { box-sizing: border-box; margin: 0; padding: 0; }
  html, body { width: 1200px; height: 371px; overflow: hidden; }
  body { background: var(--page); position: relative; font-family: "Caveat", cursive; color: var(--text); }

  .card { position: absolute; width: 188px; border-radius: 6px; background: var(--tint); box-shadow: 0 2px 5px rgba(0,0,0,.18); }
  .lilac { --tint: var(--lilac); --ink: var(--lilac-ink); }
  .aqua  { --tint: var(--aqua);  --ink: var(--aqua-ink); }
  .cream { --tint: var(--cream); --ink: var(--cream-ink); }
  .mint  { --tint: var(--mint);  --ink: var(--mint-ink); }

  /* Front */
  .front { top: 37px; height: 135px; }
  .brand { position: absolute; left: 10px; top: 12px; display: flex; align-items: center; gap: 5px; }
  .brand-dot { width: 30px; height: 30px; border-radius: 50%; background: var(--ink); }
  .brand-name { font-family: "Caveat", cursive; font-size: 15px; line-height: 14px; color: var(--name); }
  .face-art { position: absolute; right: 8px; top: 8px; width: 58px; height: 92px; border-radius: 4px;
    background: linear-gradient(180deg, rgba(0,0,0,.05), rgba(0,0,0,.12)); }
  .contact { position: absolute; left: 12px; top: 80px; font-size: 9.5px; line-height: 12px; list-style: none; }
  .contact .social { display: flex; align-items: center; gap: 3px; }
  .social-square { width: 9px; height: 9px; background: var(--aqua-ink); display: inline-block; }

  /* Back */
  .back { top: 192px; height: 131px; padding: 7px 8px 6px; }
  .back-title { font-family: "Gochi Hand", cursive; font-size: 11.5px; color: var(--ink); line-height: 13px; margin-bottom: 3px; }
  .log { width: 100%; border: 1.2px solid var(--rule); border-radius: 4px; border-collapse: separate; border-spacing: 0; font-size: 8px; color: var(--rule); }
  .log th { font-weight: 500; text-align: left; padding-left: 6px; height: 9px; line-height: 9px; }
  .log td { height: 13px; border-top: 1px solid var(--rule); }
  .log td + td, .log th + th { border-left: 1px solid var(--rule); }
  .log .c-date { width: 24%; } .log .c-time { width: 20%; }
  .log .c-check { width: 14px; border-left: none !important; }
  .box { display: block; width: 8px; height: 8px; border: 1px solid var(--rule); margin: 0 auto; }

  .divider { position: absolute; left: 874px; top: 8px; height: 355px; border-left: 2px dashed var(--divider); }
  .note { position: absolute; left: 891px; top: 42px; font-family: "Just Me Again Down Here", cursive; font-size: 17px; line-height: 17px; color: #222; }

  .menu-card { position: absolute; left: 891px; top: 93px; width: 270px; height: 188px; border-radius: 7px; background: var(--coral); box-shadow: 0 2px 5px rgba(0,0,0,.18); }
  .menu-title { position: absolute; left: 8px; top: 12px; font-family: "Gochi Hand", cursive; font-size: 22px; color: var(--coral-ink); }
  .services { position: absolute; left: 5px; top: 44px; list-style: none; font-size: 10px; line-height: 14.5px; }
  .services li { display: flex; align-items: flex-start; gap: 3px; }
  .services .box { margin: 3px 0 0; flex: none; width: 7px; height: 7px; }
  .menu-card .log { position: absolute; left: 92px; top: 9px; width: 170px; height: 168px; }
  .menu-card .log td { height: 14px; }
</style>
</head>
<body>

<!-- Fronts -->
<section class="card front lilac" style="left:33px">
  <div class="brand"><span class="brand-dot"></span><span class="brand-name">Glow Haven<br>by Marisol</span></div>
  <div class="face-art" role="img" aria-label="Hand-drawn line sketch of a face with eyelashes"></div>
  <ul class="contact"><li>48 Alder Lane Fairview, CO 80000</li><li>Contact: 555-014-2261</li><li>www.glowhavenbymarisol.com</li><li class="social"><span class="social-square"></span>www.social.example/glowhaven</li></ul>
</section>
<section class="card front aqua" style="left:241px">
  <div class="brand"><span class="brand-dot"></span><span class="brand-name">Glow Haven<br>by Marisol</span></div>
  <div class="face-art" role="img" aria-label="Hand-drawn line sketch of a face with eyelashes"></div>
  <ul class="contact"><li>48 Alder Lane Fairview, CO 80000</li><li>Contact: 555-014-2261</li><li>www.glowhavenbymarisol.com</li><li class="social"><span class="social-square"></span>www.social.example/glowhaven</li></ul>
</section>
<section class="card front cream" style="left:450px">
  <div class="brand"><span class="brand-dot"></span><span class="brand-name">Glow Haven<br>by Marisol</span></div>
  <div class="face-art" role="img" aria-label="Hand-drawn line sketch of a face with eyelashes"></div>
  <ul class="contact"><li>48 Alder Lane Fairview, CO 80000</li><li>Contact: 555-014-2261</li><li>www.glowhavenbymarisol.com</li><li class="social"><span class="social-square"></span>www.social.example/glowhaven</li></ul>
</section>
<section class="card front mint" style="left:663px">
  <div class="brand"><span class="brand-dot"></span><span class="brand-name">Glow Haven<br>by Marisol</span></div>
  <div class="face-art" role="img" aria-label="Hand-drawn line sketch of a face with eyelashes"></div>
  <ul class="contact"><li>48 Alder Lane Fairview, CO 80000</li><li>Contact: 555-014-2261</li><li>www.glowhavenbymarisol.com</li><li class="social"><span class="social-square"></span>www.social.example/glowhaven</li></ul>
</section>

<!-- Backs -->
<section class="card back lilac" style="left:33px">
  <h2 class="back-title">Need a wax ? Set up a date!</h2>
  <table class="log">
    <tr><th class="c-date">date</th><th class="c-time">time</th><th>remark</th><th class="c-check"></th></tr>
    <tr><td></td><td></td><td></td><td class="c-check"><span class="box"></span></td></tr>
    <tr><td></td><td></td><td></td><td class="c-check"><span class="box"></span></td></tr>
    <tr><td></td><td></td><td></td><td class="c-check"><span class="box"></span></td></tr>
    <tr><td></td><td></td><td></td><td class="c-check"><span class="box"></span></td></tr>
    <tr><td></td><td></td><td></td><td class="c-check"><span class="box"></span></td></tr>
    <tr><td></td><td></td><td></td><td class="c-check"><span class="box"></span></td></tr>
    <tr><td></td><td></td><td></td><td class="c-check"><span class="box"></span></td></tr>
  </table>
</section>
<section class="card back aqua" style="left:241px">
  <h2 class="back-title">Need a facial ? Set up a date!</h2>
  <table class="log">
    <tr><th class="c-date">date</th><th class="c-time">time</th><th>remark</th><th class="c-check"></th></tr>
    <tr><td></td><td></td><td></td><td class="c-check"><span class="box"></span></td></tr>
    <tr><td></td><td></td><td></td><td class="c-check"><span class="box"></span></td></tr>
    <tr><td></td><td></td><td></td><td class="c-check"><span class="box"></span></td></tr>
    <tr><td></td><td></td><td></td><td class="c-check"><span class="box"></span></td></tr>
    <tr><td></td><td></td><td></td><td class="c-check"><span class="box"></span></td></tr>
    <tr><td></td><td></td><td></td><td class="c-check"><span class="box"></span></td></tr>
    <tr><td></td><td></td><td></td><td class="c-check"><span class="box"></span></td></tr>
  </table>
</section>
<section class="card back cream" style="left:450px">
  <h2 class="back-title">Need a treatment ? Set up a date!</h2>
  <table class="log">
    <tr><th class="c-date">date</th><th class="c-time">time</th><th>remark</th><th class="c-check"></th></tr>
    <tr><td></td><td></td><td></td><td class="c-check"><span class="box"></span></td></tr>
    <tr><td></td><td></td><td></td><td class="c-check"><span class="box"></span></td></tr>
    <tr><td></td><td></td><td></td><td class="c-check"><span class="box"></span></td></tr>
    <tr><td></td><td></td><td></td><td class="c-check"><span class="box"></span></td></tr>
    <tr><td></td><td></td><td></td><td class="c-check"><span class="box"></span></td></tr>
    <tr><td></td><td></td><td></td><td class="c-check"><span class="box"></span></td></tr>
    <tr><td></td><td></td><td></td><td class="c-check"><span class="box"></span></td></tr>
  </table>
</section>
<section class="card back mint" style="left:663px">
  <h2 class="back-title">Need a body wrap ? Set up a date!</h2>
  <table class="log">
    <tr><th class="c-date">date</th><th class="c-time">time</th><th>remark</th><th class="c-check"></th></tr>
    <tr><td></td><td></td><td></td><td class="c-check"><span class="box"></span></td></tr>
    <tr><td></td><td></td><td></td><td class="c-check"><span class="box"></span></td></tr>
    <tr><td></td><td></td><td></td><td class="c-check"><span class="box"></span></td></tr>
    <tr><td></td><td></td><td></td><td class="c-check"><span class="box"></span></td></tr>
    <tr><td></td><td></td><td></td><td class="c-check"><span class="box"></span></td></tr>
    <tr><td></td><td></td><td></td><td class="c-check"><span class="box"></span></td></tr>
    <tr><td></td><td></td><td></td><td class="c-check"><span class="box"></span></td></tr>
  </table>
</section>

<div class="divider"></div>
<p class="note">or an alternative to having a different<br>colour for each different service :</p>

<section class="menu-card">
  <h2 class="menu-title">Need a :</h2>
  <ul class="services">
    <li><span class="box"></span>treatment</li>
    <li><span class="box"></span>facial</li>
    <li><span class="box"></span>chemical peel</li>
    <li><span class="box"></span>body wrap</li>
    <li><span class="box"></span>salt glow</li>
    <li><span class="box"></span>wax</li>
    <li><span class="box"></span>eyelash extensions</li>
    <li><span class="box"></span>microdermabrasion<br>treatment</li>
  </ul>
  <table class="log">
    <tr><th class="c-date">date</th><th class="c-time">time</th><th>remark</th><th class="c-check"></th></tr>
    <tr><td></td><td></td><td></td><td class="c-check"><span class="box"></span></td></tr>
    <tr><td></td><td></td><td></td><td class="c-check"><span class="box"></span></td></tr>
    <tr><td></td><td></td><td></td><td class="c-check"><span class="box"></span></td></tr>
    <tr><td></td><td></td><td></td><td class="c-check"><span class="box"></span></td></tr>
    <tr><td></td><td></td><td></td><td class="c-check"><span class="box"></span></td></tr>
    <tr><td></td><td></td><td></td><td class="c-check"><span class="box"></span></td></tr>
    <tr><td></td><td></td><td></td><td class="c-check"><span class="box"></span></td></tr>
    <tr><td></td><td></td><td></td><td class="c-check"><span class="box"></span></td></tr>
    <tr><td></td><td></td><td></td><td class="c-check"><span class="box"></span></td></tr>
    <tr><td></td><td></td><td></td><td class="c-check"><span class="box"></span></td></tr>
  </table>
</section>

</body>
</html>
```